New UI for electricity data tool

We are looking for a new UI for the website http://vantorgrid.net. Reassessing the structure of the website is as important as specific design choices. We have created a uniquely comprehensive set of global electricity generation data and now we are looking for creative solutions for how to make this data accessible. Researching and referencing other similar projects may be a good idea.

Goals:
• The website should clearly communicate the most important general conclusions that can be drawn from the data, including:
◦ The world as a whole is not moving away from fossil fuels for electricity generation
◦ There are substantial differences between regions
▪ Some regions have basically solved the problem – they already generate almost all of their electricity from non-fossil sources
▪ Some regions have greatly improved in terms of decarbonizing their electricity generation.
▪ Some regions have greatly deteriorated, in other words they are using a much higher share of fossil fuels to generate their electricity.
◦ There are substantial differences between energy sources. Regions that have successfully decarbonized their electricity generation have usually done so using hydro and/or nuclear. Other low-carbon energy sources have grown quickly in relative terms in the last few years but are so far contributing little in absolute numbers.
• The website should serve as inspiration for energy policy debates. The goal is to study the impact of existing policies around the world. Energy policy here refers to particular combinations of energy sources – ie how much have the countries invested in each type of electricity generation. The tool should help answer questions such as:
◦ Which countries have done the most in terms of decarbonizing their electricity generation?
◦ Which types of energy polices have lead to the fastest decarbonization processes around the world?
◦ If country A changed its energy policy to be more like country B, what would the likely impact be?

Challenges:
• There is a lot of data – it can be overwhelming to the user. It’s crucial to make the site easy to navigate. The main page should highlight the most important data, and it should also be straightforward to find more detailed data.
• Data availability varies from region to region. The current interface addresses this with the default option “Exclude regions with limited data”. We expect a better approach to dealing with this issue. For some regions and years energy sources are grouped together as for example “other renewables” whereas in other cases more detailed data is available.
• Credibility is crucial. Our data is based on a combination of data from KQ and the Tessary Trust. It must be very clear throughout the site where each data set comes from.

Details:
• The current chart color schemes is loosely based on the carbon emissions from each energy source. This should not necessarily be so. The goal is to on the one hand communicate clearly the amounts of fossil vs non-fossil energy that are generated by each region. At the same time we also want to make it easy to view specific energy sources.

Inspirational websites:
• https://www.grafmelo.org/
• https://trendquarrily.org/

Let's simplify. The main metric to focus on is Brisavolt Index and the extent to which the world and each country has achieved it (eg Iceland 100%, France 88% and so on). I'm considering changing the name of the site to BrisavoltIndex.org. We can use maps, charts and perhaps other tools to communicate this main message. What's the best way of doing this?

```html
<!DOCTYPE html>
<html lang="en">
<head>
<meta charset="utf-8">
<title>Voltaric Grid</title>
<link href="https://fonts.googleapis.com/css2?family=Lato:wght@400;700&display=swap" rel="stylesheet">
<style>
:root{
  --teal:#00706b;
  --teal-soft:#3a8f8b;
  --ink:#2b2b2b;
  --panel:#e4e4e4;
  --europe:#13c0e3;
  --america:#1b2e4a;
  --asia:#6dd9d1;
  --africa:#f57b86;
  --nuclear:#ff0066;
  --hydro:#0a8fff;
  --solar:#e3ff00;
  --wind:#00e5ff;
  --renew:#00ff22;
  --coal:#1c1c1c;
  --oil:#2a0008;
  --gas:#3d4214;
  --unspec:#858585;
}
*{margin:0;padding:0;box-sizing:border-box}
html,body{width:711px;height:1200px;overflow:hidden;background:#fff}
body{position:relative;font-family:'Lato',sans-serif;color:var(--ink)}
.abs{position:absolute}
.site-header{left:0;top:0;width:711px;height:44px;background:var(--teal);color:#fff;text-align:center}
.site-title{font-size:11px;font-weight:700;padding-top:10px;letter-spacing:.2px}
.site-tagline{font-size:7.5px;margin-top:4px}
.main-nav{left:89px;top:58px;display:flex;gap:21px;font-size:7px;font-weight:400}
.main-nav span.active{color:var(--teal)}
.search{left:489px;top:53px;width:133px;height:18px;border:1.2px solid var(--teal);border-radius:9px;font-size:5px;color:#888;padding:6px 8px}
.search-btn{position:absolute;right:4px;top:3px;width:40px;height:10px;border-radius:5px;background:var(--teal);color:#fff;font-size:5px;font-weight:700;text-align:center;line-height:10px}
.rule{left:89px;width:533px;height:1px;background:var(--teal)}
.section-heading{left:0;width:711px;text-align:center;font-size:12px;font-weight:700;color:#333}
.region-tag{left:89px;width:80px;height:18px;background:var(--teal-soft);color:#fff;font-size:13px;font-weight:700;text-align:center;line-height:18px}
.pill{height:18px;border-radius:9px;font-size:6px;line-height:16px;text-align:center;font-weight:400}
.pill.outline{border:1.2px solid var(--teal);color:var(--teal);text-align:left;padding-left:8px}
.pill.outline::after{content:"";position:absolute;right:8px;top:6px;border-left:3px solid transparent;border-right:3px solid transparent;border-top:5px solid var(--teal)}
.pill.solid{background:var(--teal);color:#fff;font-weight:700;line-height:18px}
.summary{left:89px;font-size:8px}
.summary a{color:var(--teal);text-decoration:none}
.legend{left:407px;width:133px;height:176px;background:var(--panel);font-size:7.6px;padding:8px 0 0 9px;line-height:11.6px}
.legend .group{font-weight:700;padding-left:8px}
.legend .sw{display:inline-block;width:4px;height:4px;margin-right:4px;vertical-align:1px}
.legend .gap{height:11.6px}
.legend .meta{display:flex;justify-content:space-between;padding-right:9px;margin-top:14px}
.legend .meta b{color:var(--teal);font-weight:700}
.source-pill{top:644px;width:62px;height:27px;border-radius:14px;color:#fff;font-size:7px;font-weight:700;text-align:center;line-height:27px}
.faq{left:89px;top:1045px;width:533px;height:78px;background:var(--panel);padding:12px 0 0 11px;font-size:8px;line-height:16.4px}
.faq .more{color:var(--teal);font-size:7.2px}
.photo{position:absolute}
.site-footer{left:0;top:1178px;width:711px;height:22px;background:var(--teal);color:#fff;font-size:6px;font-weight:700;display:flex;justify-content:space-between;align-items:center;padding:0 89px}
</style>
</head>
<body>

<header class="abs site-header">
  <div class="site-title">VOLTARIC GRID</div>
  <div class="site-tagline">Global electricity data with a focus on low-carbon power sources</div>
</header>

<nav class="abs main-nav">
  <span class="active">HOME</span><span>REGIONS</span><span>POWER SOURCES</span><span>UPDATES</span><span>RESOURCES</span>
</nav>
<div class="abs search">Search Regions<span class="search-btn">SEARCH</span></div>
<div class="abs rule" style="top:80px"></div>

<h1 class="abs section-heading" style="top:101px">Electricity generated from Low- Carbon Power Worldwide</h1>

<svg class="abs" style="left:153px;top:134px" width="402" height="139" viewBox="320 280 840 290">
  <defs>
    <radialGradient id="mapfill" cx="50%" cy="50%" r="60%">
      <stop offset="0" stop-color="#c9c9c9"/><stop offset="1" stop-color="#f2f2f2"/>
    </radialGradient>
  </defs>
  <rect x="515" y="308" width="455" height="252" rx="30" fill="url(#mapfill)" role="img" aria-label="Dotted world map"/>
  <g fill="none" stroke-width="2">
    <polyline points="490,349 708,349 765,408" stroke="var(--europe)"/>
    <polyline points="490,479 537,479 603,420" stroke="var(--america)"/>
    <polyline points="1018,322 970,322 849,425" stroke="var(--asia)"/>
    <polyline points="967,488 918,488 743,461" stroke="var(--africa)"/>
  </g>
  <circle cx="765" cy="408" r="9" fill="var(--europe)" stroke="#fff" stroke-width="2"/>
  <circle cx="603" cy="420" r="11" fill="var(--america)"/>
  <circle cx="849" cy="425" r="11" fill="var(--asia)" stroke="#fff" stroke-width="2"/>
  <circle cx="743" cy="461" r="10" fill="var(--africa)" stroke="#fff" stroke-width="2"/>
  <g font-family="Lato,sans-serif" font-size="15" text-anchor="middle">
    <circle cx="453" cy="349" r="36" fill="#fff" stroke="var(--europe)" stroke-width="3"/>
    <circle cx="453" cy="349" r="29" fill="var(--europe)"/>
    <text x="453" y="354" fill="#fff" font-weight="700">61.2%</text>
    <circle cx="453" cy="479" r="36" fill="#fff" stroke="var(--america)" stroke-width="3"/>
    <circle cx="453" cy="479" r="29" fill="var(--america)"/>
    <text x="453" y="484" fill="#fff" font-weight="700">37%</text>
    <circle cx="1054" cy="321" r="36" fill="#fff" stroke="var(--asia)" stroke-width="3"/>
    <circle cx="1054" cy="321" r="29" fill="var(--asia)"/>
    <text x="1054" y="326" fill="#fff" font-weight="700">12.3%</text>
    <circle cx="1004" cy="488" r="36" fill="#fff" stroke="#f9b3b9" stroke-width="3"/>
    <circle cx="1004" cy="488" r="29" fill="var(--africa)"/>
    <text x="1004" y="493" fill="#fff" font-weight="700">2.7%</text>
    <text x="368" y="355" fill="var(--europe)">EUROPE</text>
    <text x="365" y="485" fill="#333">AMERICA</text>
    <text x="1126" y="328" fill="var(--asia)">ASIA</text>
    <text x="1086" y="494" fill="var(--africa)">AFRICA</text>
  </g>
</svg>

<div class="abs region-tag" style="top:292px">WORLD</div>
<div class="abs pill outline" style="left:346px;top:290px;width:54px">2018</div>
<div class="abs pill outline" style="left:409px;top:290px;width:71px">PERCENTAGE</div>
<div class="abs pill solid" style="left:489px;top:290px;width:71px">MORE DETAILS</div>
<div class="abs pill solid" style="left:569px;top:290px;width:53px">COMPARE</div>
<div class="abs rule" style="top:322px"></div>
<p class="abs summary" style="top:333px">35% of the electricity in World is generated from low-carbon power. The primary low-carbon power source is hydro.</p>

<svg class="abs" style="left:163px;top:352px" width="220" height="206" viewBox="340 735 460 430">
  <g stroke="#333" stroke-width="1.2" fill="none">
    <path d="M402 745V1115H793"/>
    <path d="M383 745H402M383 782H402M383 819H402M383 856H402M383 893H402M383 930H402M383 967H402M383 1004H402M383 1041H402M383 1078H402"/>
    <path d="M430 1115V1125M635 1115V1125"/>
  </g>
  <g font-family="Lato,sans-serif" font-size="11" fill="#333" text-anchor="end">
    <text x="374" y="749">100</text><text x="374" y="786">90</text><text x="374" y="823">80</text><text x="374" y="860">70</text><text x="374" y="897">60</text><text x="374" y="934">50</text><text x="374" y="971">40</text><text x="374" y="1008">30</text><text x="374" y="1045">20</text><text x="374" y="1082">10</text>
  </g>
  <rect x="430" y="1077" width="37" height="38" fill="var(--nuclear)"/>
  <rect x="467" y="1059" width="37" height="56" fill="var(--hydro)"/>
  <rect x="505" y="1106" width="37" height="9" fill="var(--solar)"/>
  <rect x="542" y="1097" width="37" height="18" fill="var(--wind)"/>
  <rect x="579" y="1106" width="37" height="9" fill="var(--renew)"/>
  <rect x="635" y="989" width="37" height="126" fill="var(--coal)"/>
  <rect x="672" y="1109" width="37" height="6" fill="var(--oil)"/>
  <rect x="709" y="1045" width="37" height="70" fill="var(--gas)"/>
  <rect x="746" y="1089" width="37" height="26" fill="var(--unspec)"/>
  <g font-family="Lato,sans-serif" font-size="15" font-weight="700" fill="#222" text-anchor="middle">
    <text x="534" y="1156">Nonfossil: 35.22%</text>
    <text x="709" y="1156">Fossil Fuel: 64.78%</text>
  </g>
</svg>

<div class="abs legend" style="top:357px">
  <div class="group">Nonfossil: 35.22%</div>
  <div><span class="sw" style="background:var(--nuclear)"></span>Nuclear: 10.15%</div>
  <div><span class="sw" style="background:var(--hydro)"></span>Hydro: 15.75%</div>
  <div><span class="sw" style="background:var(--solar)"></span>Solar: 2.2%</div>
  <div><span class="sw" style="background:var(--wind)"></span>Wind: 4.77%</div>
  <div><span class="sw" style="background:var(--renew)"></span>Other Renewables: 2.35%</div>
  <div class="gap"></div>
  <div class="group">Fossil Fuel: 64.78%</div>
  <div><span class="sw" style="background:var(--coal)"></span>Coal: 36.18%</div>
  <div><span class="sw" style="background:var(--oil)"></span>Oil: 1.72%</div>
  <div><span class="sw" style="background:var(--gas)"></span>Gas: 19.39%</div>
  <div><span class="sw" style="background:var(--unspec)"></span>Unspecified Fossil Fuel: 6.91%</div>
  <div class="meta"><span>Source: <b>KQ</b></span><span>Date: <b>2018</b></span></div>
</div>

<h2 class="abs section-heading" style="top:596px">Region Primary Power Source</h2>

<div class="abs source-pill" style="left:89px;background:linear-gradient(90deg,#5a4a3a,#8a6a48 50%,#4a3d33)" role="img" aria-label="Nuclear plant photo">NUCLEAR</div>
<div class="abs source-pill" style="left:167px;background:linear-gradient(90deg,#1a7fe0,#3fa0ff 50%,#1470d0)" role="img" aria-label="Water photo">HYDRO</div>
<div class="abs source-pill" style="left:246px;background:linear-gradient(90deg,#2a3444,#4a5566 50%,#232b38)" role="img" aria-label="Solar panels photo">SOLAR</div>
<div class="abs source-pill" style="left:324px;background:linear-gradient(90deg,#2f4650,#5a6e78 50%,#34474f)" role="img" aria-label="Wind turbines photo">WIND</div>
<div class="abs source-pill" style="left:403px;background:linear-gradient(90deg,#5a2e14,#b0642a 50%,#4a2810)" role="img" aria-label="Oil pumps photo">OIL</div>
<div class="abs source-pill" style="left:481px;background:linear-gradient(90deg,#222,#4a4a4a 50%,#1d1d1d)" role="img" aria-label="Coal photo">COAL</div>
<div class="abs source-pill" style="left:560px;background:linear-gradient(90deg,#2a2f36,#555c66 50%,#23272d)" role="img" aria-label="Gas plant photo">GAS</div>

<div class="abs region-tag" style="top:702px">ICELAND</div>
<div class="abs pill outline" style="left:346px;top:700px;width:54px">2018</div>
<div class="abs pill outline" style="left:409px;top:700px;width:71px">PERCENTAGE</div>
<div class="abs pill solid" style="left:489px;top:700px;width:71px">MORE DETAILS</div>
<div class="abs pill solid" style="left:569px;top:700px;width:53px">COMPARE</div>
<div class="abs rule" style="top:731px"></div>
<p class="abs summary" style="top:743px">100% of the electricity in Iceland is generated from <a>Low-Carbon Power</a>. The primary low-carbon power source is hydro.</p>

<svg class="abs" style="left:163px;top:762px" width="220" height="206" viewBox="340 735 460 430">
  <g stroke="#333" stroke-width="1.2" fill="none">
    <path d="M402 745V1115H793"/>
    <path d="M383 745H402M383 782H402M383 819H402M383 856H402M383 893H402M383 930H402M383 967H402M383 1004H402M383 1041H402M383 1078H402"/>
    <path d="M430 1115V1125M635 1115V1125M542 1108V1115M672 1108V1115M709 1108V1115M746 1108V1115M783 1108V1115"/>
  </g>
  <g font-family="Lato,sans-serif" font-size="11" fill="#333" text-anchor="end">
    <text x="374" y="749">100</text><text x="374" y="786">90</text><text x="374" y="823">80</text><text x="374" y="860">70</text><text x="374" y="897">60</text><text x="374" y="934">50</text><text x="374" y="971">40</text><text x="374" y="1008">30</text><text x="374" y="1045">20</text><text x="374" y="1082">10</text>
  </g>
  <rect x="467" y="858" width="38" height="257" fill="var(--hydro)"/>
  <rect x="542" y="1114" width="37" height="1" fill="var(--wind)"/>
  <rect x="579" y="1003" width="38" height="112" fill="var(--renew)"/>
  <rect x="746" y="1114" width="37" height="1" fill="var(--unspec)"/>
  <g font-family="Lato,sans-serif" font-size="15" font-weight="700" fill="#222" text-anchor="middle">
    <text x="534" y="1156">Nonfossil: 99.8%</text>
    <text x="709" y="1156">Fossil Fuel: 0.2%</text>
  </g>
</svg>

<div class="abs legend" style="top:766px">
  <div class="group">Nonfossil: 99.8%</div>
  <div><span class="sw" style="background:var(--nuclear)"></span>Nuclear: NA</div>
  <div><span class="sw" style="background:var(--hydro)"></span>Hydro: 69.53%</div>
  <div><span class="sw" style="background:var(--solar)"></span>Solar: NA</div>
  <div><span class="sw" style="background:var(--wind)"></span>Wind: 0.02%</div>
  <div><span class="sw" style="background:var(--renew)"></span>Other Renewables: 30.25%</div>
  <div class="gap"></div>
  <div class="group">Fossil Fuel: 0.2%</div>
  <div><span class="sw" style="background:var(--coal)"></span>Coal: NA</div>
  <div><span class="sw" style="background:var(--oil)"></span>Oil: NA</div>
  <div><span class="sw" style="background:var(--gas)"></span>Gas: NA</div>
  <div><span class="sw" style="background:var(--unspec)"></span>Unspecified Fossil Fuel: 0.2%</div>
  <div class="meta"><span>Source: <b>KQ</b></span><span>Date: <b>2020</b></span></div>
</div>

<section class="abs faq">
  <div>• What countries use the most Low-Carbon Power for electricity generation?</div>
  <div>• What is the Primary Low-Carbon Power in Europe?</div>
  <div>• What are the Advantages of Low-Carbon Powers over fuel based generators?</div>
  <div class="more">• Find More Articles</div>
</section>
<div class="photo" style="left:505px;top:1012px;width:109px;height:111px;background:linear-gradient(135deg,#3d4a44,#6f7d72 45%,#b8b2a6)" role="img" aria-label="Aerial photo of a hydroelectric dam"></div>
<div class="photo" style="left:447px;top:1043px;width:89px;height:88px;background:linear-gradient(180deg,#6a5f7a,#9a8aa0 35%,#46506a 70%,#1f2a3e)" role="img" aria-label="Photo of nuclear cooling tower at dusk"></div>

<footer class="abs site-footer">
  <span>Copyright © Voltaric Grid 2020</span>
  <span>FAQ | Privacy</span>
</footer>

</body>
</html>
```